Transformative School Model Needs a Website. I am easy to work with.

Greetings:
I am creating a K-12 school that is a complete and total re-imagination of what education can be for children, families, communities, and the planet. While we will begin as a K-12 school, I really see it as a complete life cycle education (birth to death). I'm looking for a website to describe my new transformational educational model. I anticipate having 7-8 pages. I have all the copy ready.
I am the Founder. I am easy to work with, an effective communicator, and I’m very good at knowing what I want and providing specific and concrete detail, examples, and direction to make sure I use your time wisely.

```html
<!DOCTYPE html>
<html lang="en">
<head>
<meta charset="utf-8">
<title>Serene Unity Academy</title>
<link href="https://fonts.googleapis.com/css2?family=Cinzel:wght@500;600&family=Lato:wght@300;400;700&display=swap" rel="stylesheet">
<style>
:root{
  --ink:#222222;
  --text:#4a4a4a;
  --white:#ffffff;
  --sage:#b1b6a5;
  --footer:#2a2a2a;
  --field:#a9a9a9;
  --btn-dark:#2b2b2b;
}
*{box-sizing:border-box;margin:0;padding:0}
html,body{width:1200px;height:3963px;overflow:hidden;background:var(--white)}
body{font-family:'Lato',sans-serif;color:var(--ink)}
.page{position:relative;width:1200px;height:3963px;overflow:hidden}
.abs{position:absolute}
.serif{font-family:'Cinzel',serif;font-weight:600;letter-spacing:1px}
.eyebrow{font-size:25px;font-weight:400}
.heading{font-size:46px;line-height:50px}
.body-copy{font-size:15px;line-height:26px;color:var(--text);font-weight:400}
.btn{display:flex;align-items:center;justify-content:center;border:1.5px solid currentColor;font-size:18px;font-weight:700;letter-spacing:.3px;text-transform:uppercase}

/* hero */
.hero{left:0;top:0;width:1200px;height:711px;background:radial-gradient(ellipse 420px 420px at 900px 330px,#c98a52 0%,#7a4a2a 35%,rgba(25,35,20,0) 70%),linear-gradient(90deg,#141a12 0%,#24301e 50%,#3a3a22 100%)}
.brand-badge{left:112px;top:12px;width:160px;height:160px;border:2px solid var(--white);border-radius:50%;display:flex;align-items:center;justify-content:center;text-align:center;color:var(--white);font-size:17px;line-height:22px;font-family:'Cinzel',serif;font-weight:500}
.nav{left:317px;top:57px;display:flex;gap:17px;color:var(--white);font-size:16px;font-weight:400}
.nav-donate{left:981px;top:43px;width:107px;height:51px;color:var(--white);font-size:17px}
.hero-kicker{left:111px;top:246px;color:var(--white);font-size:30px;font-weight:400}
.hero-title{left:111px;top:300px;color:var(--white);font-size:66px;line-height:68px;font-weight:600}
.hero-btn{left:111px;top:541px;width:204px;height:67px;color:var(--white)}

/* philosophy */
.philosophy{left:0;top:711px;width:1200px;height:558px;background:linear-gradient(90deg,#f7f6f5 0%,#f1f1f1 60%,#e9e9e8 100%)}
.seal-art{left:100px;top:761px;width:470px;height:454px;background:radial-gradient(circle at 50% 45%,#d9a26e 0%,#a5623c 30%,#e6ddd3 62%,rgba(241,241,241,0) 75%)}
.philo-text{left:628px;top:778px;width:470px}

/* about */
.founder-photo{left:692px;top:1181px;width:431px;height:619px;background:linear-gradient(180deg,#b79a82 0%,#8a6a55 30%,#5b7550 55%,#4a6340 100%);border-radius:200px 200px 0 0}
.about-text{left:111px;top:1350px;width:570px}
.signature{left:111px;top:1622px;width:378px;height:85px;background:linear-gradient(90deg,#e8e8e8,#f4f4f4)}
.pointer{left:558px;top:1665px}

/* purpose */
.purpose{left:0;top:1800px;width:1200px;height:532px;background:var(--sage);color:var(--white);text-align:center}
.purpose-kicker{top:72px;left:0;width:1200px}
.purpose-heading{top:110px;left:0;width:1200px}
.benefit{position:absolute;top:190px;width:200px;margin-left:-100px}
.benefit-ring{width:169px;height:169px;border:2px solid var(--white);border-radius:50%;margin:0 auto;display:flex;align-items:center;justify-content:center}
.benefit-ring .inner{width:151px;height:151px;border:3px solid var(--white);border-radius:50%;display:flex;align-items:center;justify-content:center}
.benefit-ring svg{width:78px;height:78px;fill:none;stroke:var(--white);stroke-width:2.5;stroke-linecap:round;stroke-linejoin:round}
.benefit-label{margin-top:20px;font-size:19px;line-height:25px;font-weight:700}

/* equity */
.equity{left:0;top:2332px;width:1200px;height:579px;background:radial-gradient(ellipse 360px 300px at 420px 220px,#d68c45 0%,#8d5a32 40%,rgba(30,25,20,0) 80%),linear-gradient(90deg,#3a4a66 0%,#5a4a3a 40%,#2b2520 65%,#1f1c19 100%)}
.equity-text{left:694px;top:2400px;width:420px;color:var(--white)}
.equity-text .body-copy{color:var(--white)}

/* contact */
.contact-head{left:0;width:1200px;text-align:center}
.field{position:absolute;border:1px solid var(--field);font-size:15px;font-weight:400;color:#666;padding:14px 15px}
.send{left:541px;top:3393px;width:117px;height:57px;background:var(--btn-dark);color:var(--white);border:none;font-size:17px}

/* footer */
.footer{left:0;top:3538px;width:1200px;height:425px;background:var(--footer)}
.footer-badge{left:131px;top:3573px;width:258px;height:261px;border:3px solid var(--white);border-radius:50%;display:flex;align-items:center;justify-content:center;text-align:center;color:var(--white);font-family:'Cinzel',serif;font-size:26px;line-height:34px;font-weight:500}
.footer-col{color:var(--white)}
.footer-col h4{font-size:18px;font-weight:700;margin-bottom:18px;color:var(--white)}
.footer-col li{list-style:none;font-size:16px;line-height:25px;font-weight:400;color:var(--white)}
.info-row{display:flex;gap:14px;font-size:16px;line-height:23px;margin-bottom:20px}
.info-row svg{flex:none;margin-top:3px}
.divider{left:111px;top:3865px;width:975px;height:1px;background:#555}
.copyright{left:111px;top:3896px;font-size:16px;color:var(--white)}
.social{top:3882px;width:46px;height:46px;border:1.5px solid var(--white);border-radius:50%}
</style>
</head>
<body>
<div class="page">

  <!-- Hero -->
  <div class="abs hero" role="img" aria-label="Photo of a woman with eyes closed, face lifted to warm sunlight in a green garden"></div>
  <div class="abs brand-badge">Serene<br>Unity<br>Academy</div>
  <nav class="abs nav">
    <span>School Foundations</span><span>Curriculum</span><span>Pedagogy</span><span>Outcomes</span><span>Opening</span><span>Testimonials</span>
  </nav>
  <div class="abs btn nav-donate">Donate</div>
  <p class="abs hero-kicker">Welcome to</p>
  <h1 class="abs serif hero-title">SERENE<br>UNITY<br>ACADEMY</h1>
  <div class="abs btn hero-btn">Get More Info</div>

  <!-- Philosophy -->
  <div class="abs philosophy"></div>
  <div class="abs seal-art" role="img" aria-label="Large ornamental emblem in warm copper and soft ivory tones"></div>
  <div class="abs philo-text">
    <p class="eyebrow">Philosophy</p>
    <h2 class="serif heading" style="margin-top:8px">SPIRITUAL<br>PHILOSOPHY</h2>
    <p class="body-copy" style="margin-top:28px">Nemo enim ipsam voluptatem quia voluptas sit aspernatur aut odit aut fugit, sed quia consequuntur magni dolores eos qui seratione volu ptatem sequi nesciunt. Neque porro quisquam est, qui dolorem ipsum quia dolor sit amet, consectet adipisci velit, sed quia non numquam eius modi tempora incidunt ut labore et dolore magnam aliquam quaer.</p>
    <div class="btn" style="margin-top:36px;width:158px;height:59px;color:#333;font-weight:400;font-size:17px">Read More</div>
  </div>

  <!-- About -->
  <div class="abs founder-photo" role="img" aria-label="Portrait photo of the smiling founder in a green sweater, arms crossed"></div>
  <div class="abs about-text">
    <p class="eyebrow">Founder</p>
    <h2 class="serif heading" style="margin-top:6px">ABOUT ME</h2>
    <p class="body-copy" style="margin-top:22px">Nemo enim ipsam voluptatem quia voluptas sit aspernatur aut odit aut fugit, sed quia consequuntur magni dolores eos qui seratione volu ptatem sequi nesciunt. Neque porro quisquam est, qui dolorem ipsum quia dolor sit amet, consectet adipisci velit, sed quia non numquam eius modi tempora incidunt ut labore et dolore magnam aliquam quaer.</p>
  </div>
  <div class="abs signature" role="img" aria-label="Handwritten signature of Mara Ellison"></div>
  <svg class="abs pointer" width="124" height="64" viewBox="0 0 124 64" fill="none" stroke="#222" stroke-width="2.5" stroke-linecap="round">
    <path d="M118 4 C100 36 60 52 6 52"/>
    <path d="M18 40 L6 52 L20 60"/>
  </svg>

  <!-- Purpose -->
  <section class="abs purpose">
    <p class="abs eyebrow purpose-kicker">Why Us</p>
    <h2 class="abs serif heading purpose-heading">PURPOSE</h2>
    <div class="benefit" style="left:197px"><div class="benefit-ring"><div class="inner">
      <svg viewBox="0 0 80 80" aria-hidden="true"><circle cx="40" cy="40" r="26"/><path d="M40 14v52M40 40L22 58M40 40l18 18"/></svg>
    </div></div><p class="benefit-label">Gives Peace<br>of mind</p></div>
    <div class="benefit" style="left:398px"><div class="benefit-ring"><div class="inner">
      <svg viewBox="0 0 80 80" aria-hidden="true"><circle cx="40" cy="40" r="26"/><path d="M28 30l6 8-5 3 8 10M46 26l-4 9 6 2-3 9M54 40l-4 6 5 2"/></svg>
    </div></div><p class="benefit-label">Stress relief<br>mechanism</p></div>
    <div class="benefit" style="left:600px"><div class="benefit-ring"><div class="inner">
      <svg viewBox="0 0 80 80" aria-hidden="true"><path d="M40 64S14 48 14 30a12 12 0 0 1 26-6 12 12 0 0 1 26 6c0 18-26 34-26 34z"/><path d="M30 38l7 7 13-14"/></svg>
    </div></div><p class="benefit-label">Improve your<br>physical and<br>mental health</p></div>
    <div class="benefit" style="left:800px"><div class="benefit-ring"><div class="inner">
      <svg viewBox="0 0 80 80" aria-hidden="true"><path d="M44 10L24 44h14l-4 26 22-36H42z"/></svg>
    </div></div><p class="benefit-label">Increases<br>energy efficiency</p></div>
    <div class="benefit" style="left:1003px"><div class="benefit-ring"><div class="inner">
      <svg viewBox="0 0 80 80" aria-hidden="true"><circle cx="40" cy="40" r="30"/><circle cx="40" cy="40" r="21"/><path d="M40 50s-11-7-11-14a5.5 5.5 0 0 1 11-2 5.5 5.5 0 0 1 11 2c0 7-11 14-11 14z"/></svg>
    </div></div><p class="benefit-label">Divine growth of<br>mind and soul</p></div>
  </section>

  <!-- Equity -->
  <div class="abs equity" role="img" aria-label="Photo of an older couple laughing together in golden evening light"></div>
  <div class="abs equity-text">
    <p class="eyebrow">Equity</p>
    <h2 class="serif heading" style="margin-top:8px">STATEMENT OF<br>ONENESS WITH<br>EQUITY</h2>
    <p class="body-copy" style="margin-top:24px">Nemo enim ipsam voluptatem quia voluptas sit aspern atur aut odit aut fugit, sed quia consequuntur magni dolores eos qui seratione volu ptatem sequi nesciunt. Neque porro quisquam est.</p>
    <div class="btn" style="margin-top:38px;width:159px;height:57px;font-weight:400;font-size:17px">Donate</div>
  </div>

  <!-- Contact -->
  <p class="abs eyebrow contact-head" style="top:2984px;color:#444">Get In Touch</p>
  <h2 class="abs serif heading contact-head" style="top:3030px">CONTACT US</h2>
  <p class="abs contact-head" style="top:3102px;font-size:15px;font-weight:400;color:#555">Please contact us via this form and we will get back to soon</p>
  <div class="field" style="left:186px;top:3168px;width:406px;height:51px">Your Name (required)</div>
  <div class="field" style="left:186px;top:3233px;width:406px;height:51px">Your Email (required)</div>
  <div class="field" style="left:186px;top:3299px;width:406px;height:51px">Subject</div>
  <div class="field" style="left:607px;top:3168px;width:406px;height:181px">Your Message</div>
  <div class="abs btn send">Send</div>

  <!-- Footer -->
  <footer class="abs footer"></footer>
  <div class="abs footer-badge">Serene<br>Unity<br>Academy</div>
  <div class="abs footer-col" style="left:532px;top:3597px">
    <h4>Quick Links</h4>
    <ul><li>Home</li><li>School Foundations</li><li>Curriculum</li><li>Pedagogy</li><li>Outcomes</li><li>Opening</li><li>Testimonials</li></ul>
  </div>
  <div class="abs footer-col" style="left:729px;top:3597px;width:380px">
    <h4>Contact Information</h4>
    <div class="info-row"><svg width="12" height="16" viewBox="0 0 12 16"><path d="M6 0a6 6 0 0 0-6 6c0 4.5 6 10 6 10s6-5.5 6-10a6 6 0 0 0-6-6zm0 8.5A2.5 2.5 0 1 1 6 3.5a2.5 2.5 0 0 1 0 5z" fill="#fff"/></svg><span>N0: 123 uis aute irure dol in repre<br>sse cillum dolore</span></div>
    <div class="info-row"><svg width="14" height="14" viewBox="0 0 14 14"><path d="M3 0l2.5 3.5-1.5 2c1 2 2.5 3.5 4.5 4.5l2-1.5L14 11l-1.5 3C6 14 0 8 0 1.5z" fill="#fff"/></svg><span>1 555 010 0199</span></div>
    <div class="info-row"><svg width="16" height="12" viewBox="0 0 16 12"><rect width="16" height="12" rx="1" fill="#fff"/><path d="M1 1l7 5 7-5" stroke="#2a2a2a" stroke-width="1.5" fill="none"/></svg><span>info@sereneunityacademy.org</span></div>
  </div>
  <div class="abs divider"></div>
  <p class="abs copyright">© Serene Unity Academy, 2023. All Rights Reserved.</p>
  <div class="abs social" style="left:925px" role="img" aria-label="Social profile link"></div>
  <div class="abs social" style="left:983px" role="img" aria-label="Social profile link"></div>
  <div class="abs social" style="left:1040px" role="img" aria-label="Social profile link"></div>

</div>
</body>
</html>
```